Web Design Project (uncoded)

About Us
ZumLink is a telecom startup and is looking to launch its website.
ZumLink specializes in providing communication solutions to the travel market. Our mission is to develop cost effective communication products and solutions for the international traveler.
Our simple vision of "every hotel should have a mobile phone in the guest rooms", led us to develop a pathbreaking & cost effective mobile phone. With full integration capabilities with the hotels property management system, location based marketing, user locator and other features, this product is unique in addressing the hospitality segment.
The website is targeted at hotel owners and property management companies.
The website should have a young contemporary and a funky look, in line with the name.
Please find attached our logo (for the colors etc.). (attached now).
We would like to receive the design for a home page and an inside page for the website.
Site map would be as follows: Home, About Us, Solutions, Contact us
Thanks and look forward,
Tamsa
Target Market(s)
Hotel decision makers
Industry/Entity Type
Property Management
Look and feel
Each slider illustrates characteristics of the customer's brand and the style your logo design should communicate.

```html
<!DOCTYPE html>
<html lang="en">
<head>
<meta charset="utf-8">
<title>ZumLink – Telecom Services</title>
<link href="https://fonts.googleapis.com/css2?family=Questrial&family=Ubuntu:wght@300;400;500;700&display=swap" rel="stylesheet">
<style>
:root{
  --orange:#f7931e;
  --orange-light:#fbab3a;
  --orange-deep:#f07a12;
  --orange-bar:#ec6f12;
  --ink:#1c1c1c;
  --text:#333;
  --muted:#777;
  --line:#dcdcdc;
  --white:#fff;
  --panel:#f1f1f1;
}
*{margin:0;padding:0;box-sizing:border-box}
html,body{width:885px;height:1200px;overflow:hidden;background:var(--white)}
body{position:relative;font-family:"Ubuntu",sans-serif;color:var(--text)}
.abs{position:absolute}

.top-rule{left:0;top:0;width:885px;height:3px;background:#111}
.site-header{left:0;top:3px;width:885px;height:86px;background:var(--white)}
.brand{display:flex;align-items:center;gap:8px}
.brand-mark{width:50px;height:50px;border-radius:50%;background:var(--orange)}
.brand-name{font-family:"Ubuntu",sans-serif;font-weight:700;font-size:30px;color:var(--ink);letter-spacing:-1px}
.site-header .brand{position:absolute;left:28px;top:20px}
.main-nav{position:absolute;top:55px;left:552px;display:flex;gap:0}
.main-nav a{font-size:12px;color:var(--ink);text-decoration:none;font-family:"Ubuntu",sans-serif;position:absolute;white-space:nowrap}

.hero{left:0;top:89px;width:885px;height:341px;background:linear-gradient(180deg,var(--orange-light),var(--orange) 60%,var(--orange-deep))}
.hero-band{left:0;top:52px;width:613px;height:187px;background:linear-gradient(90deg,rgba(255,190,70,.55),rgba(255,170,50,.25))}
.hero-photo{left:605px;top:0;width:280px;height:341px;background:linear-gradient(180deg,#f9a640,#f0a06a 55%,#f4e6df)}
.hero-title{left:44px;top:64px;font-family:"Questrial",sans-serif;font-size:28px;color:var(--white);white-space:nowrap}
.hero-title b{font-family:"Ubuntu",sans-serif;font-weight:700;color:var(--ink)}
.hero-sub{left:45px;top:99px;font-family:"Questrial",sans-serif;font-size:17px;color:var(--white)}
.hero-text{left:43px;top:124px;width:370px;font-family:"Questrial",sans-serif;font-size:11px;line-height:15.5px;color:var(--white)}
.btn{left:43px;top:185px;width:102px;height:31px;background:#111;color:var(--white);border-radius:3px;font-family:"Questrial",sans-serif;font-size:13px;display:flex;align-items:center;justify-content:center}

.stats{left:0;top:289px;width:613px;height:52px;background:var(--orange-bar);display:flex}
.stat{width:204px;display:flex;align-items:center;gap:10px;padding-left:34px;color:var(--white);font-size:15px;font-weight:500;border-right:1px solid #d85d08}
.stat:first-child{width:216px;font-family:"Questrial",sans-serif;font-size:18px;font-weight:400}
.stat:last-child{border-right:0}

.features{left:0;top:430px;width:885px;height:156px;background:linear-gradient(180deg,#fff,#ececec)}
.feature{top:20px;width:240px}
.feature h3{display:flex;align-items:center;gap:6px;font-weight:400;font-size:17px;color:var(--ink);margin-left:-4px}
.feature p{margin:8px 0 0 32px;font-size:9.5px;line-height:17px;color:#222}
.feature p b{font-weight:500}

.card{top:605px;width:264px;height:313px;border:1px solid var(--line);border-radius:3px;background:var(--white);box-shadow:0 0 3px rgba(0,0,0,.06)}
.card h2{position:absolute;left:11px;top:13px;font-weight:400;font-size:15px;color:var(--ink)}
.card-photo{position:absolute;left:11px;top:41px;width:243px;height:95px;border:1px solid #ccc}
.card .lead{position:absolute;left:14px;top:149px;width:235px;font-size:9.5px;font-weight:500;line-height:17px;color:#222}
.card .body{position:absolute;left:14px;top:188px;width:240px;font-size:9.5px;font-weight:300;line-height:17.3px;color:var(--muted)}
.learn{position:absolute;left:15px;top:279px;display:flex;align-items:center;gap:6px;font-size:11px;font-weight:500;color:var(--orange-deep)}
.learn i{width:15px;height:15px;border-radius:50%;background:var(--orange-deep);display:flex;align-items:center;justify-content:center}

.divider{left:19px;top:955px;width:836px;border-top:1px dotted #bbb}
.foot-col{top:984px}
.foot-col h4{font-weight:400;font-size:12px;color:var(--ink);margin-bottom:10px}
.foot-col ul{list-style:none}
.foot-col li{font-size:10px;font-weight:300;color:#555;height:21.6px}
.foot-brand{left:670px;top:988px}
.copyright{left:31px;top:1153px;font-size:10px;font-weight:300;color:#555}
</style>
</head>
<body>
<div class="abs top-rule"></div>

<header class="abs site-header">
  <div class="brand"><span class="brand-mark"></span><span class="brand-name">ZumLink</span></div>
  <nav class="main-nav">
    <a style="left:0">HOME</a>
    <a style="left:59px">ABOUT US</a>
    <a style="left:139px">SOLUTIONS</a>
    <a style="left:226px">CONTACT US</a>
  </nav>
</header>

<section class="abs hero">
  <div class="abs hero-band"></div>
  <div class="abs hero-photo" role="img" aria-label="Smiling woman talking on a mobile phone over an orange world map"></div>
  <h1 class="abs hero-title"><b>ZumLink</b> Telecome Services</h1>
  <p class="abs hero-sub">your tittel line goes here</p>
  <p class="abs hero-text">Lorem ipsum dolor sit amet, consectetuer adipiscing elit. Nam cursus. Morbi ut mi. Nullam enim leo, egestas id, condimentum at, laoreet mattis, massa. Sed eleifend nonummy diam.</p>
  <div class="abs btn">learn more</div>
  <div class="abs stats">
    <div class="stat">
      <svg width="28" height="20" viewBox="0 0 28 20"><path d="M2 7c0-4 6-6 12-6s12 2 12 6l-1 3-5-1V6c-4-1-8-1-12 0v3l-5 1z" fill="#fff"/><rect x="6" y="11" width="16" height="8" rx="2" fill="#fff"/></svg>
      555 014 2260
    </div>
    <div class="stat">
      <svg width="32" height="24" viewBox="0 0 32 24"><g fill="none" stroke="#fff" stroke-width="3" stroke-linecap="round"><path d="M3 9a18 18 0 0 1 26 0"/><path d="M8 14a11 11 0 0 1 16 0"/></g><circle cx="16" cy="20" r="3" fill="#fff"/></svg>
      New Connection
    </div>
    <div class="stat">
      <svg width="28" height="28" viewBox="0 0 28 28"><circle cx="14" cy="8" r="6" fill="#fff"/><path d="M2 27c0-8 5-12 12-12s12 4 12 12z" fill="#fff"/></svg>
      24/7 Services
    </div>
  </div>
</section>

<section class="abs features">
  <div class="abs feature" style="left:33px">
    <h3><svg width="26" height="26" viewBox="0 0 26 26"><path d="M5 2l5 5-3 3c2 4 5 7 9 9l3-3 5 5-3 4C11 24 2 15 1 5z" fill="#111"/></svg>Telecom Featured</h3>
    <p><b>Lorem ipsum dolor sit amet, consectetuer adipiscing elit.</b> Morbi ut mi. Nullam enim leo, egestas id, condimentum at, laoreet mattis, massa. Sed eleifend nonummy diam.</p>
  </div>
  <div class="abs feature" style="left:339px">
    <h3><svg width="26" height="26" viewBox="0 0 26 26"><path d="M13 4L4 22M13 4l9 18" stroke="#111" stroke-width="3" fill="none"/><circle cx="13" cy="4" r="3" fill="#111"/><circle cx="4" cy="22" r="3" fill="#111"/><circle cx="22" cy="22" r="3" fill="#111"/></svg>Telecom Featured</h3>
    <p><b>Lorem ipsum dolor sit amet, consectetuer adipiscing elit.</b> Morbi ut mi. Nullam enim leo, egestas id, condimentum at, laoreet mattis, massa. Sed eleifend nonummy diam.</p>
  </div>
  <div class="abs feature" style="left:626px">
    <h3><svg width="26" height="26" viewBox="0 0 26 26"><rect x="2" y="11" width="5" height="13" fill="#111"/><path d="M9 11l5-9c2 0 3 2 2 5l-1 3h7c2 0 3 2 2 4l-3 9c-1 1-2 1-3 1H9z" fill="#111"/></svg>Telecom Featured</h3>
    <p><b>Lorem ipsum dolor sit amet, consectetuer adipiscing elit.</b> Morbi ut mi. Nullam enim leo, egestas id, condimentum at, laoreet mattis, massa. Sed eleifend nonummy diam.</p>
  </div>
</section>

<article class="abs card" style="left:26px">
  <h2>Why Chooose Us</h2>
  <div class="card-photo" role="img" aria-label="Satellite dishes against a blue sky" style="background:linear-gradient(160deg,#1e63c8,#6fa8e8 60%,#dfe9f3)"></div>
  <p class="lead">Lorem ipsum dolor sit amet, consectetuer adipiscing elit.</p>
  <p class="body">Nam cursus. Morbi ut mi. Nullam enim leo, egestas id, condimentum at, laoreet mattis, massa. Sed eleifend nonummy diam. Praesent mauris ante, elementum et, bibendum at, posuere sit amet, nibh. Duis tincidunt lectus quis dui viverra vestibulum. Suspendisse</p>
  <div class="learn">Learn more <i><svg width="7" height="8" viewBox="0 0 7 8"><path d="M0 0l7 4-7 4z" fill="#fff"/></svg></i></div>
</article>
<article class="abs card" style="left:307px">
  <h2>Support &amp; Services</h2>
  <div class="card-photo" role="img" aria-label="Call centre staff wearing headsets" style="background:linear-gradient(90deg,#e9e4df,#cfc7c0 50%,#eef0f2)"></div>
  <p class="lead">Lorem ipsum dolor sit amet, consectetuer adipiscing elit.</p>
  <p class="body">Nam cursus. Morbi ut mi. Nullam enim leo, egestas id, condimentum at, laoreet mattis, massa. Sed eleifend nonummy diam. Praesent mauris ante, elementum et, bibendum at, posuere sit amet, nibh. Duis tincidunt lectus quis dui viverra vestibulum. Suspendisse</p>
  <div class="learn">Learn more <i><svg width="7" height="8" viewBox="0 0 7 8"><path d="M0 0l7 4-7 4z" fill="#fff"/></svg></i></div>
</article>
<article class="abs card" style="left:586px">
  <h2>Customer Testimonials</h2>
  <div class="card-photo" role="img" aria-label="Business people meeting around a table" style="background:linear-gradient(90deg,#dfe3e6,#4a4a4f 45%,#e6e6e6 70%,#2a2a2e)"></div>
  <p class="lead">Lorem ipsum dolor sit amet, consectetuer adipiscing elit.</p>
  <p class="body">Nam cursus. Morbi ut mi. Nullam enim leo, egestas id, condimentum at, laoreet mattis, massa. Sed eleifend nonummy diam. Praesent mauris ante, elementum et, bibendum at, posuere sit amet, nibh. Duis tincidunt lectus quis dui viverra vestibulum. Suspendisse</p>
  <div class="learn">Learn more <i><svg width="7" height="8" viewBox="0 0 7 8"><path d="M0 0l7 4-7 4z" fill="#fff"/></svg></i></div>
</article>

<div class="abs divider"></div>

<footer>
  <div class="abs foot-col" style="left:35px"><h4>Company</h4><ul><li>Why choose ZumLink?</li><li>Why We Are</li><li>Jobs</li><li>Press News</li><li>Our Technology</li></ul></div>
  <div class="abs foot-col" style="left:162px"><h4>Why We Are</h4><ul><li>&nbsp;Comany</li><li>&nbsp;Mission</li><li>&nbsp;Services Overview</li><li>&nbsp;What We Do</li><li>&nbsp;Our Plans</li></ul></div>
  <div class="abs foot-col" style="left:293px"><h4>Support</h4><ul><li>Support</li><li>FAQ</li><li>Customer Services</li><li>24/7 Support</li><li>Location</li></ul></div>
  <div class="abs foot-col" style="left:412px;top:982px"><h4>Contact</h4><ul><li>&nbsp;Testimonials</li><li>&nbsp;Recent Blog</li><li>&nbsp;Contact Form</li><li>&nbsp;Contact Us</li></ul></div>
  <div class="abs foot-col" style="left:524px;top:982px"><h4>Services</h4><ul><li>Sub Menu First</li><li>Sub Menu Second</li><li>Sub Menu third</li><li>Sub Menu Fouth</li></ul></div>
  <div class="abs brand foot-brand"><span class="brand-mark" style="width:54px;height:54px"></span><span class="brand-name">ZumLink</span></div>
  <p class="abs copyright">© 2012 Company Name &nbsp;|&nbsp; All right reserved &nbsp;|&nbsp; Term &amp; Conditions</p>
</footer>
</body>
</html>
```